Take a look!!! A Broadway-style Musical needs a dynamic poster design!

We need a poster design for the Broadway musical - SKILLETVILLE.
Synopsis:
SkilletVille is a delicious musical comedy set in Chicago. When Lenny McBrask, a timid fry cook accidentally invents the hottest new craze in the fast-food world; the Crescent Patty, he takes the humble SKILLETVILLE diner from its lowly place beneath the tracks of the Marwick elevated train station to soaring new heights. Along the way, LENNY encounters bad guys, big business, beautiful women, and burgers. He struggles to hold onto his sanity as he chases his dreams.
SKILLETVILLE is a cutie little show with a simple plot about the evils of corruption and the temptations and allures of big franchise money... the show looks to have a future throughout America where we can relate to the concepts the show reminds us of so lovingly.

More info: The show is a musical. It is a comedy... with a little drama. Beautiful music. It has been performed throughout the world.

It is set in the present , but definitely has the feel of the 1950's American burger joints.

Main Characters:
LENNY MC BRASK (m)………………A young inventive nerd, LENNY is sincere, caring and kind. He works as a fry cook at SkilletVille. LENNY wants to be successful, but he doesn’t have a clue where to start. He is in love with MAE, but he only admires her from a distance. Once, in high school, LENNY tried to kiss a girl and was immediately struck with “hysterical lockjaw.” His dating life has only gone downhill since then.

GUS TORTELLA (m)………………….The stingy and cranky owner of SkilletVille. GUS borrowed money from the mob to save his failing restaurant but the lack of constant customers has his blood pressure at an all time high. When asked which two men he admired most, TORTELLA answered, “Ebenezer Scrooge and myself.”

MAE DUBRINSKA (w)………………A lovely young waitress who has worked at the SkilletVille diner since it opened. For the last two years, Mae has also been taking classes to become a dental hygienist. She is very sweet and has often found herself without train fare because she has given her money away to the needy. MAE has a thing for LENNY, but she’s afraid to get too close. One time, she touched his hand while he was cooking and he accidentally caught his apron on fire. MAE’S biggest desire in life is to bring happiness to everyone…hopefully including herself.

TRIXIE VANTELL (w)……………….A sexy beauty who looks out for Number One. Trixie is crowned “Miss SkilletVille” by GUS, who hopes her “assets” will increase business at the diner. TRIXIE began her climb to the top as a stripper, who was best known for her use of balloons and a live badger. After her badger was hit by a Winnebago, TRIXIE moved on to beauty pageants and reality television. Nothing has ever stopped her from trying to achieve her dream of becoming the “wealthiest diva in the world.” Her preference is to reach her goal still wearing all of her clothing.

Plus an additional 5 person ensemble of 2 men and women that play a multitude of roles from customers to newspaper reporters.

Reason: This musical is slated for a major production in New York, and therefore the designs need producer approval. More time is needed to review the wonderful work being submitted.

Target Market(s)

Broadway audiences

Industry/Entity Type

Entertainment Industry

Requirements
Must have
• SKILLETVILLE, the musical
• Book by Hal Bixby
• Music by Corin Faldt Lyrics by Margot Bixby
Nice to have
• Fun. Colorful. A nod to the Burger joints of the past. 50's American Drive Thru Diner.
• Also.. maybe center around the image of a burger... or someone cooking a burger... or running with a burger on a plate... It can be funny...
Should not have
• Important: Use the photos that are attached just to get an idea of the colors and the feel of the show... don't use the actual photos in the poster design. It is fair game to create caricatures from the images but not actual photo.

```html
<!DOCTYPE html>
<html lang="en">
<head>
<meta charset="utf-8">
<title>SkilletVille – The Musical</title>
<link href="https://fonts.googleapis.com/css2?family=Jost:wght@300;400&display=swap" rel="stylesheet">
<style>
  :root {
    --stage: #e2e2e2;
    --poster-black: #000;
    --glow-teal: rgba(20, 150, 170, 0.75);
    --glow-blue: rgba(40, 60, 130, 0.6);
    --glow-purple: rgba(150, 30, 150, 0.8);
    --glow-amber: rgba(150, 75, 20, 0.7);
    --neon-white: #ffffff;
    --neon-blue: #2fb8ff;
    --text-soft: #f2f2f2;
    --staff-line: rgba(255, 255, 255, 0.35);
  }
  html, body {
    margin: 0;
    width: 1200px;
    height: 1200px;
    overflow: hidden;
    background: var(--stage);
  }
  .poster {
    position: absolute;
    left: 217px;
    top: 56px;
    width: 766px;
    height: 1084px;
    background:
      radial-gradient(circle at 78% 38%, var(--glow-teal) 0, transparent 32%),
      radial-gradient(circle at 48% 45%, var(--glow-blue) 0, transparent 40%),
      radial-gradient(circle at 88% 63%, var(--glow-purple) 0, transparent 30%),
      radial-gradient(circle at 12% 70%, var(--glow-amber) 0, transparent 30%),
      var(--poster-black);
    overflow: hidden;
    font-family: "Jost", sans-serif;
    color: var(--text-soft);
  }
  .neon-frame {
    position: absolute;
    left: 0;
    top: 0;
  }
  .hero-burger {
    position: absolute;
    left: 198px;
    top: 195px;
    width: 402px;
    height: 512px;
    border-radius: 48% 48% 44% 44% / 40% 40% 34% 34%;
    background: linear-gradient(180deg,
      #f4f4f4 0%, #ececec 12%, #c98a45 20%, #1a1a1a 30%, #5cb23a 42%,
      #e4344c 50%, #f0d060 56%, #5a3324 64%, #6cbc40 72%, #d7913e 84%, #b8732f 100%);
    filter: blur(1px);
    opacity: 0.92;
  }
  .title {
    position: absolute;
    left: 0;
    right: 0;
    top: 722px;
    margin: 0;
    text-align: center;
    font-weight: 300;
    font-size: 90px;
    line-height: 1;
    letter-spacing: 1px;
    color: #fff;
    text-shadow: 0 0 6px rgba(255,255,255,0.8), 0 0 18px rgba(255,255,255,0.35);
  }
  .subtitle {
    position: absolute;
    left: 155px;
    width: 450px;
    top: 832px;
    height: 34px;
    text-align: center;
    font-size: 25px;
    font-weight: 400;
    letter-spacing: 15px;
    line-height: 34px;
    text-indent: 15px;
    margin: 0;
    background:
      linear-gradient(var(--staff-line), var(--staff-line)) 0 0 / 100% 1px no-repeat,
      linear-gradient(var(--staff-line), var(--staff-line)) 0 5px / 100% 1px no-repeat,
      linear-gradient(var(--staff-line), var(--staff-line)) 0 28px / 100% 1px no-repeat,
      linear-gradient(var(--staff-line), var(--staff-line)) 0 33px / 100% 1px no-repeat;
  }
  .subtitle span {
    background: var(--poster-black);
    padding: 0 4px;
  }
  .credits {
    position: absolute;
    left: 0;
    right: 0;
    top: 916px;
    text-align: center;
  }
  .credit-book {
    margin: 0;
    font-size: 18px;
    letter-spacing: 0.8px;
  }
  .credit-music {
    margin: 8px 0 0;
    font-size: 12.5px;
    letter-spacing: 0.8px;
  }
</style>
</head>
<body>
  <main class="poster">
    <svg class="neon-frame" width="766" height="1084" viewBox="0 0 766 1084" aria-hidden="true">
      <defs>
        <filter id="neon-glow" x="-20%" y="-20%" width="140%" height="140%">
          <feGaussianBlur stdDeviation="6" result="blur"/>
          <feMerge><feMergeNode in="blur"/><feMergeNode in="blur"/><feMergeNode in="SourceGraphic"/></feMerge>
        </filter>
      </defs>
      <polygon class="neon-blue" points="272,174 73,636 312,636" fill="none" stroke="var(--neon-blue)" stroke-width="6" filter="url(#neon-glow)"/>
      <polygon class="neon-white" points="198,154 676,430 213,690" fill="none" stroke="var(--neon-white)" stroke-width="6" filter="url(#neon-glow)"/>
    </svg>

    <div class="hero-burger" role="img" aria-label="Cartoon burger character wearing a chef hat, sunglasses reflecting a city skyline, a halo and a devil horn, with a heart-shaped tomato slice"></div>

    <h1 class="title">SKILLETVILLE</h1>
    <p class="subtitle"><span>THE MUSICAL</span></p>

    <div class="credits">
      <p class="credit-book">BOOK BY HAL BIXBY</p>
      <p class="credit-music">MUSIC BY CORIN FALDT LYRICS BY MARGOT BIXBY</p>
    </div>
  </main>
</body>
</html>
```